Can you create a flyer 4 by 5 for Marvane Bin Cleaning Here is to Schedule an appointment. Using the attached as guidnance but make way nicer and professional? Please make it front and back.

```html
<!DOCTYPE html>
<html lang="en">
<head>
<meta charset="utf-8">
<title>Marvane Bin Cleaning – Flyer Front and Back</title>
<link href="https://fonts.googleapis.com/css2?family=Bebas+Neue&family=Arimo:ital,wght@0,700;1,700&family=Roboto+Condensed:ital,wght@1,500&display=swap" rel="stylesheet">
<style>
  :root {
    --backdrop: #cccccc;
    --card: #ffffff;
    --ink: #333333;
    --band: #808080;
    --on-band: #ffffff;
    --blue-bin: #3d8fd9;
    --blue-bin-light: #8fd0f4;
    --green-bin: #5aa64a;
    --green-bin-light: #b9dcae;
  }
  * { margin: 0; padding: 0; box-sizing: border-box; }
  html, body {
    width: 1200px; height: 709px; overflow: hidden;
    background: var(--backdrop);
  }
  .sheet { position: relative; width: 1200px; height: 709px; }

  .flyer {
    position: absolute; top: 186px; width: 405px; height: 315px;
    background: var(--card);
    box-shadow: 0 6px 14px rgba(0,0,0,.18);
  }
  .flyer::after {
    content: ""; position: absolute; left: -2px; right: 0; bottom: -8px; height: 8px;
    background: var(--band);
  }
  .flyer--front { left: 143px; }
  .flyer--back  { left: 579px; }

  .flyer > * { position: absolute; }

  .title-bar { background: var(--band); }
  .title {
    font-family: "Bebas Neue", "Oswald", sans-serif;
    color: var(--ink); white-space: nowrap; line-height: 1;
    text-align: center; left: 0; width: 100%;
  }
  .tagline {
    font-family: "Arimo", Arial, sans-serif; font-weight: 700; font-style: italic;
    color: var(--ink); white-space: nowrap; text-align: center; left: 0; width: 100%;
  }
  .cta {
    font-family: "Arimo", Arial, sans-serif; font-weight: 700;
    color: var(--ink); white-space: nowrap; line-height: 1;
  }
  .cta-sub {
    font-family: "Roboto Condensed", "Arial Narrow", sans-serif; font-weight: 500; font-style: italic;
    color: var(--ink); white-space: nowrap; line-height: 1;
  }
  .promise {
    font-family: "Arimo", Arial, sans-serif; font-weight: 700; font-style: italic;
    color: var(--ink); white-space: nowrap; line-height: 1;
  }
  .slogan {
    font-family: "Arimo", Arial, sans-serif; font-weight: 700;
    color: var(--ink); white-space: nowrap; line-height: 1;
  }

  /* Front */
  .flyer--front .title-bar { left: 13px; top: 23px; width: 379px; height: 16px; }
  .flyer--front .title { top: 19px; font-size: 41px; letter-spacing: .3px; }
  .flyer--front .tagline { top: 60px; font-size: 10.5px; }
  .flyer--front .cta { left: 16px; top: 92px; font-size: 25px; }
  .flyer--front .cta-sub { left: 17px; top: 121px; font-size: 21px; }
  .flyer--front .promise { left: 159px; top: 256px; font-size: 17.5px; }
  .flyer--front .slogan { left: 159px; top: 276px; font-size: 18px; }

  .mascot { border-radius: 18px; }
  .mascot--blue {
    left: 10px; top: 146px; width: 158px; height: 155px;
    background: radial-gradient(circle at 50% 50%, var(--blue-bin) 0%, var(--blue-bin-light) 62%, rgba(255,255,255,0) 75%);
  }
  .mascot--green {
    left: 218px; top: 79px; width: 173px; height: 158px;
    background: radial-gradient(circle at 62% 48%, var(--green-bin) 0%, var(--green-bin-light) 60%, rgba(255,255,255,0) 75%);
  }

  /* Back */
  .flyer--back .title-bar { left: 8px; top: 32px; width: 383px; height: 18px; }
  .flyer--back .title { top: 16px; font-size: 58px; }
  .flyer--back .tagline { top: 79px; font-size: 13.5px; }
  .info-band {
    left: 0; top: 111px; width: 100%; height: 107px;
    background: var(--band); text-align: center;
  }
  .info-band .cta { display: block; color: var(--on-band); font-size: 39px; margin-top: 15px; }
  .info-band .cta-sub { display: block; color: var(--on-band); font-size: 30px; margin-top: 8px; }
  .flyer--back .promise { left: 0; width: 100%; text-align: center; top: 236px; font-size: 26px; }
  .flyer--back .slogan { left: 0; width: 100%; text-align: center; top: 265px; font-size: 26px; padding-right: 20px; }
</style>
</head>
<body>
<main class="sheet">

  <section class="flyer flyer--front" aria-label="Flyer front">
    <div class="title-bar"></div>
    <h1 class="title">Marvane Bin Cleaning</h1>
    <p class="tagline">TWO LOCAL TEENS. ONE DIRTY JOB. ALL YEAR ROUND</p>
    <p class="cta">BOOK TODAY!</p>
    <p class="cta-sub">Fast, Affordable, and Local</p>
    <div class="mascot mascot--green" role="img" aria-label="Cartoon green wheelie bin holding a pressure washer wand with soap bubbles"></div>
    <div class="mascot mascot--blue" role="img" aria-label="Cartoon blue wheelie bin covered in soap bubbles, arms open"></div>
    <p class="promise">CLEAN CANS GUARNTEED</p>
    <p class="slogan">SO FRESH, SO CLEAN</p>
  </section>

  <section class="flyer flyer--back" aria-label="Flyer back">
    <div class="title-bar"></div>
    <h2 class="title">Scan to Book</h2>
    <p class="tagline">TWO LOCAL TEENS. ONE DIRTY JOB. ALL YEAR ROUND</p>
    <div class="info-band">
      <span class="cta">BOOK TODAY!</span>
      <span class="cta-sub">Fast, Affordable, and Local</span>
    </div>
    <p class="promise">CLEAN CANS GUARNTEED</p>
    <p class="slogan">SO FRESH, SO CLEAN</p>
  </section>

</main>
</body>
</html>
```